Keelbrook Vault Holdings Needs A Website

We are looking for a website for a new company. 4 Pages

Needs to be responsive and mobile friendly for all browsers and coded for both Android & IOS. SEO is also important.

Website Brief – Keelbrook Vault Holdings
Domain: www.keelbrookvault.net
Email: info@keelbrookvault.net
Phone: to be inserted later
Address: 40837 52 Ave, Edmonton, AB T6K 3R8
Platform: WordPress (recommended for flexibility, SEO tools, and ease of editing)
Requirements:
• Responsive & mobile-friendly (Android & iOS)
• Cross-browser compatibility
• Fast page load speed
• SEO optimized for storage development, management, and investment keywords
• Easy in-house editing after launch
• Professional, modern, trust-driven design reflecting expertise, reliability, and innovation
________________________________________
Pages
1. HOME
Purpose: Quickly communicate who Keelbrook Vault Holdings is and why they’re the best choice for designing, building, leasing, and managing self storage facilities.
Content Highlights:
• Hero Section: Large, bold image of a modern self storage facility with headline:
"From Concept to Capacity – Your Self Storage Experts"
• Subheadline: “Keelbrook Vault Holdings delivers turnkey design, construction, leasing, and management services for profitable self storage operations.”
• Quick Service Icons:
o Facility Design & Development
o Construction & Build Management
o Lease-Up & Marketing
o Ongoing Facility Management
• Call to Action Button: “LEARN MORE” → links to ABOUT US page.
• Featured Project Highlights: Showcase a few completed or current projects with photos and stats.
• Contact Banner: “Ready to build your next self storage project? Let’s talk.” → CONTACT page.
2. ABOUT US
Purpose: Build credibility, showcase experience, and explain the value proposition.
Content Highlights:
• Who We Are: Overview of Keelbrook Vault Holdings’ history, mission, and team expertise.
• Our Approach: End-to-end process from site selection to occupancy.
• Why Choose Us:
o Industry expertise in self storage
o Proven track record in lease-up success
o Strong vendor and contractor network
3. SERVICES
Purpose: Detail all service offerings with clarity and authority.
Sections:
• Design & Development: Market analysis, site planning, and architectural design.
• Construction Management: Overseeing timelines, budgets, and quality control.
• Lease-Up Strategy: Marketing, promotions, and occupancy acceleration.
• Ongoing Facility Management: Staffing, maintenance, revenue optimization.

4. CONTACT
Purpose: Provide simple, direct ways to connect.
Content Highlights:
• Contact Form (Name, Email, Phone, Message)
• Direct Email: info@keelbrookvault.net
• Phone (if applicable)
• Google Map embed (if there’s a head office location)
• CTA: “Let’s Build Your Storage Success Story.”
Design & Technical Notes
• Visual Style: Clean, modern, bold typography, professional color palette (to be based on branding), strong imagery of self storage facilities.
• Performance: Image compression, caching, responsive scaling.
• SEO Targets: “Self storage facility developer,” “self storage construction,” “self storage management company,” “lease-up services for self storage.”

WordPress or Joomla – must be desktop and mobile friendly with fast page load speed. Need the ability to edit ourselves.

Use pantone colours - #033c5a – dark blue
#2baadf – light blue

```html
<!DOCTYPE html>
<html lang="en">
<head>
<meta charset="utf-8">
<title>Keelbrook Vault Holdings – Self Storage Experts</title>
<link href="https://fonts.googleapis.com/css2?family=Montserrat:wght@400;500;600;700&display=swap" rel="stylesheet">
<style>
:root{
  --dark:#033c5a;
  --light:#2baadf;
  --ink:#0c2f47;
  --text:#4a5866;
  --white:#ffffff;
  --footer:#08304a;
}
*{margin:0;padding:0;box-sizing:border-box}
html,body{width:1200px;height:3856px;overflow:hidden}
body{position:relative;font-family:"Montserrat",sans-serif;background:var(--white);color:var(--text)}
.abs{position:absolute}
a{text-decoration:none;color:inherit}

/* header */
.site-header{position:absolute;left:0;top:0;width:1200px;height:70px;background:var(--white);z-index:5}
.brand{position:absolute;display:flex;align-items:center;gap:10px;font-weight:700;color:var(--dark)}
.brand-name{display:block;line-height:19px}
.brand-square{width:30px;height:30px;background:var(--dark);border-radius:3px;flex:none}
.site-header .brand{left:102px;top:16px;font-size:17px}
.main-nav{position:absolute;top:29px;left:0;font-size:14px;font-weight:600;color:var(--ink)}
.main-nav a{position:absolute;white-space:nowrap;transform:translateX(-50%)}
.main-nav .active{color:var(--light)}
.main-nav .sep{position:absolute;top:3px;width:1px;height:12px;background:var(--light)}
.header-mail{position:absolute;left:863px;top:22px;display:flex;align-items:center;gap:10px;font-size:14px;font-weight:600;color:var(--ink)}
.icon-circle{width:28px;height:28px;border-radius:50%;background:var(--light);display:flex;align-items:center;justify-content:center}

/* hero */
.hero-photo{position:absolute;left:0;top:70px;width:1200px;height:690px;
  background:linear-gradient(90deg,#4b8fbf 0%,#a9c7dd 18%,#e8eef3 40%,#eef2f5 60%,#c9cfd3 78%,#8d8a74 100%)}
.hero-copy{position:absolute;left:0;top:168px;width:1200px;text-align:center}
.hero-copy h1{font-size:39px;font-weight:700;line-height:48px;color:var(--dark)}
.hero-copy h1 span{display:block;color:var(--light)}
.hero-copy p{margin:24px auto 0;width:460px;font-size:17px;line-height:23px;color:#2d3a45}
.btn{position:absolute;display:flex;align-items:center;justify-content:center;gap:8px;border-radius:24px;font-size:14px;font-weight:700;color:var(--white);letter-spacing:.3px}
.btn-dark{background:var(--dark)}
.btn-light{background:var(--light)}

/* services */
.services-shape{position:absolute;left:0;top:600px;width:1200px;height:596px}
.section-eyebrow{position:absolute;left:0;width:1200px;text-align:center;font-size:13px;letter-spacing:.3px;color:var(--light)}
.section-title{position:absolute;left:0;width:1200px;text-align:center;font-size:39px;font-weight:700}
.hex{position:absolute;width:226px;height:260px}
.hex .hex-shape{position:absolute;left:0;top:0}
.hex-label{position:absolute;left:0;top:123px;width:226px;text-align:center;font-size:17px;font-weight:700;line-height:22px;color:var(--white)}
.hex-label::after{content:"";display:block;width:26px;height:3px;margin:10px auto 0;background:var(--light)}
.hex.is-active .hex-label::after{background:var(--white)}
.hex .hex-icon{position:absolute;left:91px;top:64px}

/* projects */
.project-photo{position:absolute;width:560px;height:433px}
.project-frame{position:absolute;width:112px;height:351px;background:var(--light)}
.project-card{position:absolute;width:516px;height:329px;background:var(--white);box-shadow:0 6px 22px rgba(3,60,90,.13);padding:40px 34px 0 51px}
.project-card::before{content:"";position:absolute;left:0;top:30px;width:3px;height:40px;background:var(--light)}
.project-card h3{font-size:26px;font-weight:700;color:var(--dark)}
.project-card p{margin-top:16px;width:416px;font-size:13.5px;line-height:19.5px;color:#53606b}
.stats{margin-top:28px;display:grid;grid-template-columns:156px 146px 1fr;width:430px}
.stat{font-size:13.5px;line-height:17px;color:#3d4a55;padding:0 0 16px 3px;white-space:nowrap}
.stat strong{display:block;font-weight:700;color:var(--ink)}
.stat:nth-child(3n+2),.stat:nth-child(3n){border-left:1px solid var(--light);padding-left:14px}
.stat:nth-child(-n+3){border-bottom:1px solid var(--light)}
.stat:nth-child(n+4){padding-top:18px}

/* cta */
.cta{position:absolute;left:0;top:2943px;width:1200px;height:506px;background:linear-gradient(90deg,#1c8fc4,#2baadf 60%,#3ab4e4)}
.cta-photo{position:absolute;left:0;top:0;width:1200px;height:506px;
  background:linear-gradient(135deg,#e9eef2,#cdd6de 55%,#a9b3bb);clip-path:polygon(718px 0,1200px 0,1200px 506px,556px 506px)}
.cta-eyebrow{position:absolute;left:139px;top:124px;font-size:16px;color:var(--white)}
.cta h2{position:absolute;left:141px;top:160px;font-size:33px;line-height:44px;font-weight:700;color:var(--white)}

/* footer */
.site-footer{position:absolute;left:0;top:3449px;width:1200px;height:407px;background:var(--footer);color:var(--white)}
.footer-rule{position:absolute;top:0;width:1px;height:314px;background:rgba(255,255,255,.14)}
.site-footer .brand{left:135px;top:62px;font-size:17px;color:var(--white)}
.site-footer .brand-square{background:var(--white)}
.social{position:absolute;top:141px;width:40px;height:40px;border-radius:50%;border:2px solid rgba(255,255,255,.55)}
.social.is-active{background:var(--light);border-color:var(--light)}
.footer-col{position:absolute;top:64px}
.footer-col h4{font-size:16px;font-weight:700;letter-spacing:.3px;position:relative}
.footer-col h4::before{content:"";position:absolute;left:-30px;top:0;width:3px;height:20px;background:var(--light)}
.footer-col ul{list-style:none;margin-top:14px}
.footer-col li{font-size:13.5px;line-height:24.5px;padding-left:12px;position:relative}
.footer-col li::before{content:"";position:absolute;left:0;top:10px;width:4px;height:4px;background:var(--light)}
.contact-line{display:flex;gap:12px;font-size:14px;line-height:20px;margin-top:14px}
.contact-line .icon-circle{width:26px;height:26px;flex:none;background:var(--white)}
.copyright{position:absolute;left:0;top:314px;width:1200px;height:93px;border-top:1px solid rgba(255,255,255,.14);text-align:center;padding-top:34px;font-size:13px;color:rgba(255,255,255,.85)}
</style>
</head>
<body>

<header class="site-header">
  <a class="brand" href="#"><span class="brand-square"></span><span><span class="brand-name">Keelbrook Vault</span><span class="brand-name">Holdings</span></span></a>
  <nav class="main-nav">
    <a class="active" href="#" style="left:389px">HOME</a>
    <span class="sep" style="left:440px"></span>
    <a href="#" style="left:508px">ABOUT US</a>
    <span class="sep" style="left:578px"></span>
    <a href="#" style="left:640px">SERVICES</a>
    <span class="sep" style="left:709px"></span>
    <a href="#" style="left:770px">CONTACT</a>
  </nav>
  <a class="header-mail" href="#">
    <span class="icon-circle"><svg width="14" height="10" viewBox="0 0 14 10"><rect x="0.5" y="0.5" width="13" height="9" rx="1" fill="#fff"/><path d="M1 1l6 5 6-5" stroke="#2baadf" stroke-width="1.3" fill="none"/></svg></span>
    info@keelbrookvault.net
  </a>
</header>

<section class="hero">
  <div class="hero-photo" role="img" aria-label="Bright self storage corridor with blue roll-up doors and a site supervisor in a hard hat reviewing a tablet"></div>
  <div class="hero-copy">
    <h1>From Concept to Capacity<span>Your Self Storage Experts</span></h1>
    <p>Keelbrook Vault Holdings delivers turnkey design, construction, leasing, and management services for profitable self storage operations.</p>
  </div>
  <a class="btn btn-dark" href="#" style="left:510px;top:381px;width:174px;height:43px">CONTACT US <span>›</span></a>
</section>

<section class="services">
  <svg class="services-shape" viewBox="0 0 1200 596" aria-hidden="true">
    <defs>
      <linearGradient id="servicesBg" x1="0" y1="0" x2="0" y2="1">
        <stop offset="0" stop-color="#03466a"/><stop offset="1" stop-color="#033c5a"/>
      </linearGradient>
    </defs>
    <polygon points="0,140 600,35 1200,140 1200,596 0,596" fill="url(#servicesBg)"/>
    <polygon points="172,100 600,17 1032,100 1032,112 600,30 172,112" fill="#2baadf"/>
  </svg>
  <svg class="abs" style="left:591px;top:693px" width="28" height="10" viewBox="0 0 28 10"><path d="M2 8 Q14 -2 26 8" stroke="#fff" stroke-width="3" fill="none"/></svg>
  <div class="section-eyebrow" style="top:708px">WHAT WE DO</div>
  <h2 class="section-title" style="top:719px;color:#fff">Our Services</h2>
  <svg class="abs" style="left:540px;top:766px" width="120" height="12" viewBox="0 0 120 12"><path d="M2 10 Q60 -2 118 6" stroke="#2baadf" stroke-width="3" fill="none"/></svg>

  <div class="hex" style="left:126px;top:808px">
    <svg class="hex-shape" width="226" height="260" viewBox="0 0 226 260"><polygon points="113,1 225,65 225,195 113,259 1,195 1,65" fill="none" stroke="rgba(255,255,255,.8)" stroke-width="1.3"/></svg>
    <svg class="hex-icon" width="44" height="44" viewBox="0 0 44 44" fill="none" stroke="#fff" stroke-width="2"><rect x="3" y="4" width="17" height="34"/><rect x="24" y="4" width="17" height="34"/><line x1="3" y1="14" x2="20" y2="14"/><line x1="24" y1="14" x2="41" y2="14"/><line x1="3" y1="42" x2="41" y2="42"/></svg>
    <div class="hex-label">Facility Design &amp;<br>Development</div>
  </div>
  <div class="hex is-active" style="left:366px;top:808px">
    <svg class="hex-shape" width="226" height="260" viewBox="0 0 226 260"><polygon points="113,0 226,65 226,195 113,260 0,195 0,65" fill="#2baadf"/></svg>
    <svg class="hex-icon" width="44" height="44" viewBox="0 0 44 44" fill="none" stroke="#fff" stroke-width="2"><rect x="4" y="8" width="32" height="30"/><line x1="4" y1="18" x2="36" y2="18"/><path d="M12 30l10-10 6 6"/><line x1="30" y1="4" x2="40" y2="14"/></svg>
    <div class="hex-label">Construction &amp; Build<br>Management</div>
  </div>
  <div class="hex" style="left:607px;top:808px">
    <svg class="hex-shape" width="226" height="260" viewBox="0 0 226 260"><polygon points="113,1 225,65 225,195 113,259 1,195 1,65" fill="none" stroke="rgba(255,255,255,.8)" stroke-width="1.3"/></svg>
    <svg class="hex-icon" width="44" height="44" viewBox="0 0 44 44" fill="none" stroke="#fff" stroke-width="2"><circle cx="28" cy="16" r="8"/><path d="M4 34h10l8 4 14-6"/><path d="M4 28h12l6 4"/></svg>
    <div class="hex-label">Lease-Up &amp;<br>Marketing</div>
  </div>
  <div class="hex" style="left:847px;top:808px">
    <svg class="hex-shape" width="226" height="260" viewBox="0 0 226 260"><polygon points="113,1 225,65 225,195 113,259 1,195 1,65" fill="none" stroke="rgba(255,255,255,.8)" stroke-width="1.3"/></svg>
    <svg class="hex-icon" width="44" height="44" viewBox="0 0 44 44" fill="none" stroke="#fff" stroke-width="2"><rect x="6" y="4" width="22" height="36"/><line x1="11" y1="12" x2="22" y2="12"/><line x1="11" y1="20" x2="22" y2="20"/><circle cx="33" cy="24" r="6"/></svg>
    <div class="hex-label">Ongoing Facility<br>Management</div>
  </div>

  <a class="btn btn-light" href="#" style="left:519px;top:1094px;width:163px;height:43px">LEARN MORE <span>›</span></a>
</section>

<section class="projects">
  <svg class="abs" style="left:586px;top:1253px" width="28" height="10" viewBox="0 0 28 10"><path d="M2 8 Q14 -2 26 8" stroke="#2baadf" stroke-width="3" fill="none"/></svg>
  <div class="section-eyebrow" style="top:1271px">COMPLETE PROJECTS</div>
  <h2 class="section-title" style="top:1288px;color:var(--dark);font-size:35px">Featured Projects</h2>
  <div class="abs" style="left:577px;top:1337px;width:46px;height:3px;background:var(--light)"></div>

  <div class="project-photo" style="left:127px;top:1395px;background:linear-gradient(90deg,#6a4220,#b9773a 25%,#d9d2c6 50%,#b9773a 75%,#6a4220)" role="img" aria-label="Indoor storage hallway lined with wooden locker doors"></div>
  <div class="project-frame" style="left:1016px;top:1434px"></div>
  <article class="project-card" style="left:603px;top:1444px">
    <h3>Project Heading</h3>
    <p>Lorem ipsum dolor sit amet, consectetur adipiscing elit, sed do eiusmod tempor incididunt ut labore et dolore magna aliqua. Quis ipsum suspendisse ultrices gravida.</p>
    <div class="stats">
      <div class="stat"><strong>24/7</strong>Access &amp; Security</div>
      <div class="stat"><strong>10,000+</strong>Storage units</div>
      <div class="stat"><strong>30%</strong>Repeat Renters</div>
      <div class="stat"><strong>500,000 sq. ft</strong>storage space</div>
      <div class="stat"><strong>#1 Rated</strong>local self-storage</div>
      <div class="stat"><strong>9%</strong>Satisfaction</div>
    </div>
  </article>

  <div class="project-photo" style="left:584px;top:1864px;background:linear-gradient(90deg,#2f5fa8,#a9b8cc 35%,#e7eaee 55%,#9fb2cc 75%,#2f5fa8)" role="img" aria-label="Long storage corridor with blue roll-up unit doors"></div>
  <div class="project-frame" style="left:129px;top:1905px"></div>
  <article class="project-card" style="left:138px;top:1915px">
    <h3>Project Heading</h3>
    <p>Lorem ipsum dolor sit amet, consectetur adipiscing elit, sed do eiusmod tempor incididunt ut labore et dolore magna aliqua. Quis ipsum suspendisse ultrices gravida.</p>
    <div class="stats">
      <div class="stat"><strong>24/7</strong>Access &amp; Security</div>
      <div class="stat"><strong>10,000+</strong>Storage units</div>
      <div class="stat"><strong>30%</strong>Repeat Renters</div>
      <div class="stat"><strong>500,000 sq. ft</strong>storage space</div>
      <div class="stat"><strong>#1 Rated</strong>local self-storage</div>
      <div class="stat"><strong>9%</strong>Satisfaction</div>
    </div>
  </article>

  <div class="project-photo" style="left:132px;top:2355px;background:linear-gradient(180deg,#1e2226,#3b4045 45%,#55595d 75%,#c9c9c9)" role="img" aria-label="Room of dark grey metal storage lockers under strip lighting"></div>
  <div class="project-frame" style="left:1019px;top:2394px"></div>
  <article class="project-card" style="left:607px;top:2404px">
    <h3>Project Heading</h3>
    <p>Lorem ipsum dolor sit amet, consectetur adipiscing elit, sed do eiusmod tempor incididunt ut labore et dolore magna aliqua. Quis ipsum suspendisse ultrices gravida.</p>
    <div class="stats">
      <div class="stat"><strong>24/7</strong>Access &amp; Security</div>
      <div class="stat"><strong>10,000+</strong>Storage units</div>
      <div class="stat"><strong>30%</strong>Repeat Renters</div>
      <div class="stat"><strong>500,000 sq. ft</strong>storage space</div>
      <div class="stat"><strong>#1 Rated</strong>local self-storage</div>
      <div class="stat"><strong>9%</strong>Satisfaction</div>
    </div>
  </article>

  <a class="btn btn-light" href="#" style="left:527px;top:2823px;width:161px;height:43px">VIEW MORE <span>›</span></a>
</section>

<section class="cta">
  <div class="cta-photo" role="img" aria-label="Hands reviewing architectural blueprints with a calculator and hard hat on the table"></div>
  <svg class="abs" style="left:141px;top:104px" width="28" height="10" viewBox="0 0 28 10"><path d="M2 8 Q14 -2 26 8" stroke="#fff" stroke-width="3" fill="none"/></svg>
  <div class="cta-eyebrow">CONTACT US</div>
  <h2>Ready to Build your<br>Next Self Storage Project?<br>Let’s talk.</h2>
  <a class="btn btn-dark" href="#" style="left:144px;top:308px;width:167px;height:45px">CONTACT US <span>›</span></a>
</section>

<footer class="site-footer">
  <span class="footer-rule" style="left:383px"></span>
  <span class="footer-rule" style="left:584px"></span>
  <span class="footer-rule" style="left:863px"></span>

  <a class="brand" href="#"><span class="brand-square"></span><span><span class="brand-name">Keelbrook Vault</span><span class="brand-name">Holdings</span></span></a>
  <span class="social is-active" style="left:134px"></span>
  <span class="social" style="left:182px"></span>
  <span class="social" style="left:230px"></span>
  <span class="social" style="left:278px"></span>

  <div class="footer-col" style="left:414px">
    <h4>NAVIGATION</h4>
    <ul><li>Home</li><li>About Us</li><li>Service</li><li>Contact us</li></ul>
  </div>
  <div class="footer-col" style="left:615px">
    <h4>SERVICES</h4>
    <ul><li>Design &amp; Development</li><li>Construction Management</li><li>Lease-Up Strategy</li><li>Ongoing Facility Management</li></ul>
  </div>
  <div class="footer-col" style="left:886px">
    <h4>CONTACT US</h4>
    <div class="contact-line">
      <span class="icon-circle"><svg width="13" height="9" viewBox="0 0 14 10"><rect x="0.5" y="0.5" width="13" height="9" rx="1" fill="#08304a"/><path d="M1 1l6 5 6-5" stroke="#fff" stroke-width="1.2" fill="none"/></svg></span>
      <span style="padding-top:3px">info@keelbrookvault.net</span>
    </div>
    <div class="contact-line">
      <span class="icon-circle"><svg width="11" height="14" viewBox="0 0 11 14"><path d="M5.5 13.5S1 8.5 1 5.5a4.5 4.5 0 0 1 9 0c0 3-4.5 8-4.5 8z" fill="#08304a"/><circle cx="5.5" cy="5.5" r="1.7" fill="#fff"/></svg></span>
      <span>40837 52 Ave, Edmonton,<br>AB T6K 3R8</span>
    </div>
  </div>

  <div class="copyright">Copyright © 2025 Keelbrook Vault Holdings. All Right Reserved</div>
</footer>

</body>
</html>
```